WordPress Site That Reviews Footwear

We need a wordpress web design for an affiliate site called TarnWisp. We review and do roundups on footwear products. The final design should be clean and mobile friendly. The site should be built with Gutenberg page builder. We like the design of https://petalharvin.com/.

Target Market(s)

USA

Industry/Entity Type

Footwear

Logo Text

TarnWisp

Number of Pages Required

4 page

Font styles to use
Serif
Sans Serif

Requirements
Must have
• Wordpress site
Blog post
Page
Categories
Homepage

```html
<!DOCTYPE html>
<html lang="en">
<head>
<meta charset="utf-8">
<title>TarnWisp – Blogs</title>
<link href="https://fonts.googleapis.com/css2?family=Jost:wght@400;500;600;700&display=swap" rel="stylesheet">
<style>
:root{
  --blue:#1f4fb0;
  --navy:#0d2f73;
  --ink:#111111;
  --text:#222222;
  --white:#ffffff;
  --footer:#050505;
  --muted:#d9d9d9;
}
*{margin:0;padding:0;box-sizing:border-box}
html,body{width:763px;height:1200px;overflow:hidden;background:var(--white)}
body{position:relative;font-family:'Jost',sans-serif;color:var(--text)}
.site-header{position:absolute;top:0;left:0;width:763px;height:56px;background:var(--white)}
.brand{position:absolute;left:56px;top:14px;display:flex;align-items:center;gap:5px;color:var(--blue);font-weight:700;font-size:20px;letter-spacing:.3px}
.brand-dot{width:12px;height:12px;border-radius:50%;background:var(--blue)}
.main-nav{position:absolute;top:23px;left:297px;display:flex;gap:21px;font-size:8.3px;letter-spacing:.8px;font-weight:500;color:var(--ink)}
.main-nav .active{color:var(--blue);border-bottom:1.5px solid var(--blue);padding-bottom:3px}
.social{position:absolute;top:24px;left:644px;display:flex;gap:10px}
.social span{width:9px;height:9px;border-radius:50%;background:var(--ink)}
.social span.alt{background:var(--blue)}
.hero{position:absolute;top:56px;left:0;width:763px;height:97px}
.hero h1{position:absolute;top:26px;width:100%;text-align:center;color:var(--white);font-size:23px;font-weight:600}
.photo{position:absolute}
.photo-main{left:56px;top:201px;width:651px;height:203px;background:linear-gradient(100deg,#5b8fc2 0%,#2f69a6 40%,#c8282f 60%,#e7e3dc 75%,#3f76b0 100%)}
.post-date{position:absolute;left:63px;top:419px;width:43px;height:34px;border-right:1px solid #e4e4e4;text-align:center}
.post-date .day{display:block;color:var(--blue);font-size:19px;font-weight:600;line-height:1}
.post-date .mon{display:block;font-size:6.5px;color:#555;margin-top:2px}
.post-title{position:absolute;left:117px;top:425px;font-size:13px;font-weight:500;color:var(--ink)}
.copy{position:absolute;left:56px;width:640px;font-size:8.7px;line-height:12.7px}
.copy p+p{margin-top:12.7px}
.photo-side{left:56px;top:574px;width:315px;height:188px;background:linear-gradient(120deg,#6e5c70 0%,#3d3548 45%,#7a7a99 70%,#2a2430 100%)}
.side-text{position:absolute;left:392px;top:597px;width:298px;font-size:8.7px;line-height:12.7px}
.side-text h2{font-size:11.2px;font-weight:500;line-height:15.2px;color:var(--ink);margin-bottom:6px}
.side-text p+p{margin-top:12.7px}
.points{position:absolute;left:70px;top:852px;list-style:none;font-size:8.7px;line-height:12.7px}
.points li{padding-left:8px;position:relative}
.points li::before{content:"";position:absolute;left:1px;top:4.5px;border-left:3px solid var(--navy);border-top:2.5px solid transparent;border-bottom:2.5px solid transparent}
.site-footer{position:absolute;top:995px;left:0;width:763px;height:178px;background:var(--footer);color:var(--muted)}
.footer-brand{position:absolute;left:56px;top:46px;display:flex;align-items:center;gap:5px;color:var(--blue);font-weight:700;font-size:19px}
.footer-social{position:absolute;left:64px;top:181px;display:flex;gap:16px}
.footer-social span{width:9px;height:9px;border-radius:50%;background:var(--white)}
.footer-social span.alt{background:var(--blue)}
.footer-col h3{color:var(--blue);font-size:11px;font-weight:500;margin-bottom:10px}
.quick-links{position:absolute;left:209px;top:36px;font-size:8.5px;line-height:16.8px}
.quick-links ul{list-style:none}
.quick-links .current{color:var(--blue);text-decoration:underline}
.contact-info{position:absolute;left:326px;top:36px;font-size:8.5px;line-height:12.7px;color:var(--white)}
.contact-row{display:flex;gap:9px;margin-bottom:12px}
.contact-row svg{flex:none;margin-top:1px}
.map{position:absolute;left:509px;top:36px;width:198px;height:111px;border-radius:4px;background:linear-gradient(135deg,#f1f1ef,#e3e6ea)}
.copyright{position:absolute;top:1173px;left:0;width:763px;height:27px;background:var(--blue);color:var(--white);font-size:8px;text-align:center;line-height:27px}
</style>
</head>
<body>
<header class="site-header">
  <div class="brand"><span class="brand-dot"></span>TarnWisp</div>
  <nav class="main-nav">
    <span>HOME</span><span>ABOUT</span><span>PRODUCTS</span><span>REVIEWS</span><span class="active">BLOGS</span><span>CONTACT US</span>
  </nav>
  <div class="social"><span></span><span></span><span class="alt"></span><span></span></div>
</header>

<section class="hero">
  <svg width="763" height="97" viewBox="0 0 763 97" aria-hidden="true">
    <defs><linearGradient id="heroFill" x1="0" y1="0" x2="1" y2="1"><stop offset="0" stop-color="#0b2a68"/><stop offset="1" stop-color="#15408f"/></linearGradient></defs>
    <path d="M0 0H763V97Q600 80 381 82Q160 84 0 97Z" fill="url(#heroFill)"/>
  </svg>
  <h1>Blogs</h1>
</section>

<div class="photo photo-main" role="img" aria-label="Pair of red, black and white high-top sneakers on a blue court"></div>

<div class="post-date"><span class="day">18</span><span class="mon">Jul, 21</span></div>
<h2 class="post-title">Lorem Ipsum is simply dummy text of the printing</h2>

<div class="copy" style="top:464px">
  <p>Lorem Ipsum is simply dummy text of the printing and typesetting industry. Lorem Ipsum has been the industry's standard dummy text ever since the 1500s, when an unknown printer took a galley of type and scrambled it to make a type specimen book. It has survived not only five centuries, but also the leap into electronic typesetting, remaining essentially unchanged.</p>
  <p>It was popularised in the 1960s with the release of Letraset sheets containing Lorem Ipsum passages, and more recently with desktop publishing software like Aldus PageMaker including versions of Lorem Ipsum.</p>
</div>

<div class="photo photo-side" role="img" aria-label="Grey canvas sneakers hanging by their laces from a wooden fence"></div>
<div class="side-text">
  <h2>Lorem Ipsum is simply dummy text of the printing and typesetting industry.</h2>
  <p>Lorem Ipsum has been the industry's standard dummy text ever since the 1500s, when an unknown printer took a galley of type and scrambled it to make a type specimen book. It has survived not only five centuries, but also the leap into electronic typesetting, remaining essentially unchanged.</p>
  <p>It was popularised in the 1960s with the release of Letraset sheets containing Lorem Ipsum passages, and more recently with desktop publishing software like Aldus PageMaker including versions of Lorem Ipsum.</p>
</div>

<div class="copy" style="top:794px">
  <p>Lorem Ipsum is simply dummy text of the printing and typesetting industry. Lorem Ipsum has been the industry's standard dummy text ever since the 1500s, when an unknown printer took a galley of type and scrambled it to make a type specimen book. It has survived not only five centuries, but also the leap into electronic typesetting, remaining essentially unchanged.</p>
</div>
<ul class="points">
  <li>Etiam quis nulla non quam congue placerat ut vitae turpis.</li>
  <li>Sed porta purus ut orci auctor, eget pulvinar augue fermentum.</li>
  <li>Nulla eu mauris vel felis congue faucibus.</li>
  <li>Proin eget quam maximus, hendrerit lectus ut, facilisis quam.</li>
</ul>
<div class="copy" style="top:921px">
  <p>It was popularised in the 1960s with the release of Letraset sheets containing Lorem Ipsum passages, and more recently with desktop publishing software like Aldus PageMaker including versions of Lorem Ipsum.</p>
</div>

<footer class="site-footer">
  <div class="footer-brand"><span class="brand-dot"></span>TarnWisp</div>
  <div class="footer-social" style="top:181px;position:absolute"></div>
  <div style="position:absolute;left:64px;top:106px;display:flex;gap:16px">
    <span style="width:9px;height:9px;border-radius:50%;background:#fff"></span>
    <span style="width:9px;height:9px;border-radius:50%;background:#fff"></span>
    <span style="width:9px;height:9px;border-radius:50%;background:var(--blue)"></span>
    <span style="width:9px;height:9px;border-radius:50%;background:#fff"></span>
  </div>
  <div class="footer-col quick-links">
    <h3>Quick Link</h3>
    <ul><li class="current">Home</li><li>About Us</li><li>Products</li><li>Testimonials</li><li>Blogs</li><li>Contact Us</li></ul>
  </div>
  <div class="footer-col contact-info">
    <h3>Conatct info</h3>
    <div class="contact-row">
      <svg width="9" height="12" viewBox="0 0 9 12" aria-hidden="true"><path d="M4.5 0A4.5 4.5 0 0 0 0 4.5C0 8 4.5 12 4.5 12S9 8 9 4.5A4.5 4.5 0 0 0 4.5 0Z" fill="#1f4fb0"/><circle cx="4.5" cy="4.5" r="1.7" fill="#050505"/></svg>
      <span>lorem ipsum, 82 Harbor Lane<br>Millbrook, NL&nbsp;&nbsp;&nbsp;A2B 3D4</span>
    </div>
    <div class="contact-row">
      <svg width="9" height="9" viewBox="0 0 10 10" aria-hidden="true"><path d="M2 0L4 2.5 3 4Q4.5 6.5 6 7L7.5 6 10 8 8.5 10Q3 9.5 0 1.5Z" fill="#1f4fb0"/></svg>
      <span>555.210.4830</span>
    </div>
    <div class="contact-row">
      <svg width="10" height="8" viewBox="0 0 10 8" aria-hidden="true"><rect width="10" height="8" fill="#1f4fb0"/><path d="M0 0L5 4.5 10 0" stroke="#050505" fill="none"/></svg>
      <span>info@tarnwisp.com</span>
    </div>
  </div>
  <div class="map" role="img" aria-label="Street map showing the store location"></div>
</footer>
<div class="copyright">Copyright © 2021 TarnWisp. All Rights Reserved</div>
</body>
</html>
```